Veterinary Business cards

Redesign Business Card

Information needed on Card:
Hours: Mon-Fri: 4pm -10PM; Sat- Sun- 10 AM- 5PM
Help@bayfernvet.com
www.bayfernvet.com
555-718-2946
4173 SE 19th Ave. okc, ok 73958
*No appointment necessary*

Optional:
Our tag line is "We're here when you need us" - If it fits on the cards.

```html
<!DOCTYPE html>
<html lang="en">
<head>
<meta charset="utf-8">
<title>Bayfern Urgent Care – Business Card</title>
<link href="https://fonts.googleapis.com/css2?family=Montserrat:wght@400;500;600&display=swap" rel="stylesheet">
<style>
  :root {
    --backdrop: #e6ebf0;
    --card: #f7f9fb;
    --orange: #cd7a27;
    --navy: #23446c;
    --white: #ffffff;
  }
  * { margin: 0; padding: 0; box-sizing: border-box; }
  html, body {
    width: 1200px; height: 900px; overflow: hidden;
    background: var(--backdrop);
    font-family: "Montserrat", sans-serif;
  }
  .card {
    position: absolute; left: 147px; top: 181px;
    width: 905px; height: 541px;
    background: var(--card);
    border: 2px solid var(--white);
    border-radius: 10px;
    overflow: hidden;
    box-shadow: 0 2px 10px rgba(30, 50, 80, 0.08);
  }
  .brand {
    position: absolute; left: 0; right: 0; top: 0; height: 285px;
    display: flex; flex-direction: column; align-items: center; justify-content: center;
    gap: 18px;
  }
  .brand-lockup {
    display: flex; align-items: center; gap: 16px;
  }
  .brand-dot {
    width: 22px; height: 22px; border-radius: 50%;
    background: var(--orange);
  }
  .brand-name {
    font-weight: 500; font-size: 46px; letter-spacing: 1px;
    color: var(--navy);
  }
  .walk-in-note {
    font-size: 18px; font-weight: 500; letter-spacing: 0.5px;
    color: var(--orange);
  }
  .tagline-band {
    position: absolute; left: 0; right: 0; top: 285px; height: 56px;
    background: var(--orange);
    display: flex; align-items: center; justify-content: center;
    color: var(--white); font-size: 20px; font-weight: 400;
  }
  .contact-panel {
    position: absolute; left: 0; right: 0; top: 342px; height: 161px;
    background: var(--navy);
  }
  .person {
    position: absolute; right: 451px; top: 36px;
    text-align: right; color: var(--white);
  }
  .person-name {
    color: var(--orange); font-weight: 600; font-size: 34px; line-height: 40px;
  }
  .person-role, .person-address { font-size: 20px; line-height: 28px; }
  .divider {
    position: absolute; left: 476px; top: 46px; width: 1.5px; height: 78px;
    background: var(--orange);
  }
  .contacts {
    position: absolute; left: 502px; top: 40px; list-style: none;
    color: var(--white); font-size: 20px;
  }
  .contacts li {
    display: flex; align-items: center; gap: 16px; height: 32px;
  }
  .contacts svg { width: 20px; height: 20px; fill: var(--orange); }
  .hours-band {
    position: absolute; left: 0; right: 0; bottom: 0; height: 37px;
    background: var(--orange);
    display: flex; align-items: center; justify-content: center; gap: 18px;
    color: var(--white); font-size: 20px;
  }
  .hours-sep { width: 7px; height: 7px; border-radius: 50%; background: var(--white); }
</style>
</head>
<body>
  <section class="card">
    <header class="brand">
      <div class="brand-lockup">
        <span class="brand-dot"></span>
        <span class="brand-name">Bayfern Urgent Care</span>
      </div>
      <p class="walk-in-note">*No appointment necessary*</p>
    </header>

    <div class="tagline-band">We're here when you need us</div>

    <div class="contact-panel">
      <div class="person">
        <div class="person-name">Daria Holt</div>
        <div class="person-role">CEO &amp; Founder</div>
        <div class="person-address">4173 SE 19th Ave. okc, ok 73958</div>
      </div>
      <div class="divider"></div>
      <ul class="contacts">
        <li>
          <svg viewBox="0 0 20 20" aria-hidden="true"><path d="M2 8c0-3 3-4 8-4s8 1 8 4v2h-4V8H6v2H2zM4 11h12l1 6H3zm6 1.5a2 2 0 1 0 0 4a2 2 0 0 0 0-4z"/></svg>
          <span>555-718-2946</span>
        </li>
        <li>
          <svg viewBox="0 0 20 20" aria-hidden="true"><path d="M2 5h16v1.5l-8 5-8-5zM2 8.5l8 5 8-5V15H2z"/></svg>
          <span>Help@bayfernvet.com</span>
        </li>
        <li>
          <svg viewBox="0 0 20 20" aria-hidden="true"><circle cx="10" cy="10" r="8"/><path d="M6 6c2 0 3 1 2 3s1 3 0 5M13 4c-1 2 1 3 3 3" stroke="#23446c" stroke-width="1.5" fill="none"/></svg>
          <span>www.bayfernvet.com</span>
        </li>
      </ul>
    </div>

    <footer class="hours-band">
      <span>Mon-Fri: 4pm -10PM</span>
      <span class="hours-sep"></span>
      <span>Sat- Sun- 10 AM- 5PM</span>
    </footer>
  </section>
</body>
</html>
```